" MINHA EMPRESA É PRESTADORA DE SERVIÇOS PARA ORGÃOS PUBLICOS, TRABALHAMOS EM VARIOS SEGMENTOS, SERVIÇOS DE REFORMA EM GERAL, FORNECIMENTO DE MATERIAL DE CONSTRUÇÃO, REALIZAÇÃO DE EVENTOS, DETRE VARIOS OUTROS MAIS. "

```html
<!DOCTYPE html>
<html lang="pt-BR">
<head>
<meta charset="utf-8">
<title>Norvaly – Papel Timbrado</title>
<link href="https://fonts.googleapis.com/css2?family=Montserrat:wght@400;600;800&display=swap" rel="stylesheet">
<style>
  :root {
    --navy: #1c2541;
    --teal: #2aa7a8;
    --paper: #ffffff;
    --backdrop: #e4e4e4;
    --ghost: #f1f2f4;
  }
  html, body {
    margin: 0;
    width: 1200px;
    height: 1200px;
    overflow: hidden;
    background: var(--backdrop);
    font-family: "Montserrat", sans-serif;
  }
  .letterhead {
    position: absolute;
    left: 264px;
    top: 125px;
    width: 672px;
    height: 948px;
    background: var(--paper);
    box-shadow: 0 6px 18px rgba(0,0,0,0.18);
    overflow: hidden;
  }
  .top-band {
    position: absolute;
    left: 0; top: 0;
    width: 100%;
    height: 7px;
    background: var(--teal);
  }
  .brand {
    position: absolute;
    top: 92px;
    left: 0;
    width: 100%;
    text-align: center;
  }
  .brand-name {
    margin: 0;
    font-weight: 800;
    font-size: 34px;
    letter-spacing: 2px;
    color: var(--navy);
    line-height: 1;
  }
  .brand-tagline {
    margin: 8px 0 0;
    font-weight: 400;
    font-size: 11px;
    letter-spacing: 3px;
    color: var(--teal);
    text-transform: uppercase;
  }
  .ghost-name {
    position: absolute;
    top: 420px;
    left: 0;
    width: 100%;
    text-align: center;
    font-weight: 800;
    font-size: 110px;
    letter-spacing: 4px;
    color: var(--ghost);
    line-height: 1;
  }
  .contact {
    position: absolute;
    top: 870px;
    left: 0;
    width: 100%;
    text-align: center;
    font-weight: 600;
    font-size: 9.5px;
    line-height: 14px;
    color: var(--navy);
  }
  .contact p { margin: 0; }
  .footer-name {
    position: absolute;
    left: 12px;
    bottom: 14px;
    margin: 0;
    font-weight: 800;
    font-size: 28px;
    letter-spacing: 1px;
    color: var(--navy);
    line-height: 1;
  }
  .bottom-band {
    position: absolute;
    left: 165px;
    right: 0;
    bottom: 8px;
    height: 5px;
    background: var(--teal);
  }
</style>
</head>
<body>
  <main class="letterhead">
    <div class="top-band"></div>

    <header class="brand">
      <h1 class="brand-name">NORVALY</h1>
      <p class="brand-tagline">Comércio e Serviços</p>
    </header>

    <div class="ghost-name" aria-hidden="true">NORVALY</div>

    <footer class="contact">
      <p>www.norvaly.com.br</p>
      <p>Rua do projeto, 00 Centro - Cidade - Estado - Cep. 00.000-000</p>
      <p>(71) 0000-0000</p>
      <p>contato@norvaly.com.br</p>
    </footer>

    <p class="footer-name">NORVALY</p>
    <div class="bottom-band"></div>
  </main>
</body>
</html>
```